Flyer für Sternenhimmel-Beobachtungen
Zielgruppe
Mit Fox Moor biete ich geführte Sternenhimmel-Beobachtungen in Lütkau (Wendelfurt) an.
Die Teilnehmer erhalten interessante Informationen über den aktuellen Sternenhimmel, astronomische Ereignisse und besondere Himmelsobjekte.
Mit einem großen Teleskop und Ferngläsern beobachten wir Objekte unseres Sonnensystems sowie Sterne, Doppelsterne, Sternhaufen, Nebel und Galaxien.
Je nach Jahreszeit dauern die Touren zwischen 1 und 2 Stunden.
Ausrüstung, Stühle, Decken, Snacks und Tee werden von mir bereitgestellt.
Aufgabenstellung
Gerne maximal 2 Seiten. Mit Informationen auf Vorderseite und Rückseite.

```html
<!DOCTYPE html>
<html lang="de">
<head>
<meta charset="utf-8">
<title>Fox Moor – Geführte Sternenbeobachtung</title>
<link rel="stylesheet" href="https://fonts.googleapis.com/css2?family=Quicksand:wght@500;600;700&family=Lato:wght@400;700&display=swap">
<style>
  :root {
    --space-deep: #0e0d14;
    --space-mid: #2a2230;
    --nebula-rose: #7a3a55;
    --nebula-violet: #5a4a78;
    --teal: #5cbcb0;
    --teal-dark: #1f5f5c;
    --teal-light: #9fe0d4;
    --mist: #c9d0d2;
    --white: #ffffff;
  }
  * { margin: 0; padding: 0; box-sizing: border-box; }
  html, body { width: 1200px; height: 849px; overflow: hidden; background: var(--space-deep); }
  .flyer {
    position: relative; width: 1200px; height: 849px; overflow: hidden;
    font-family: "Lato", Arial, sans-serif; color: var(--white);
  }
  .sky {
    position: absolute; inset: 0;
    background:
      radial-gradient(ellipse 260px 300px at 700px 400px, rgba(200,120,150,.55), transparent 70%),
      radial-gradient(ellipse 420px 380px at 720px 380px, var(--nebula-violet), transparent 75%),
      radial-gradient(ellipse 520px 460px at 740px 420px, var(--nebula-rose), transparent 80%),
      linear-gradient(160deg, var(--space-mid), var(--space-deep));
  }
  .info-panel { position: absolute; inset: 0; width: 640px; height: 849px; }
  .info-text { position: absolute; left: 0; top: 0; width: 560px; }
  .info-heading {
    position: absolute; font-family: "Quicksand", sans-serif; font-weight: 700;
    font-size: 28px; line-height: 1; white-space: nowrap;
  }
  .info-body {
    position: absolute; left: 69px; font-size: 19.5px; line-height: 31.8px; white-space: nowrap;
  }
  .info-body-compact { line-height: 29px; }
  .brand-badge { position: absolute; left: 810px; top: 41px; width: 326px; height: 326px; }
  .brand-name {
    position: absolute; left: 810px; top: 176px; width: 326px; text-align: center;
    font-family: "Quicksand", sans-serif; font-weight: 700; font-size: 46px; color: var(--white);
  }
  .portrait {
    position: absolute; left: 569px; top: 499px; width: 184px; height: 184px; border-radius: 50%;
    border: 4px solid var(--teal-light);
    background: radial-gradient(circle at 50% 40%, #7d8a78, #3b463c 60%, #1c201c);
  }
  .contact { position: absolute; left: 772px; display: flex; align-items: center; gap: 20px;
    font-family: "Quicksand", sans-serif; font-weight: 500; font-size: 24px; }
  .contact-icon { width: 54px; height: 54px; }
  .contact-mail { top: 553px; }
  .contact-phone { top: 621px; }
  .closing {
    position: absolute; left: 540px; top: 722px; width: 602px; text-align: center;
    font-family: "Quicksand", sans-serif; font-weight: 700; font-size: 27px; line-height: 46px;
  }
</style>
</head>
<body>
<main class="flyer">
  <div class="sky" role="img" aria-label="Foto eines farbigen Emissionsnebels vor dunklem Sternenhimmel"></div>

  <svg class="info-panel" viewBox="0 0 640 849" aria-hidden="true">
    <defs>
      <linearGradient id="panelFill" x1="0" y1="0" x2="1" y2="0">
        <stop offset="0" stop-color="#5cbcb0"/>
        <stop offset="0.55" stop-color="#93c4bd" stop-opacity="0.92"/>
        <stop offset="1" stop-color="#c9d0d2" stop-opacity="0.78"/>
      </linearGradient>
    </defs>
    <polygon points="0,0 630,0 505,849 0,849" fill="url(#panelFill)"/>
  </svg>

  <section class="info-text">
    <h2 class="info-heading" style="left:44px; top:38px;">Über mich</h2>
    <p class="info-body" style="top:62px;">
      Meine Begeisterung für die Astronomie begleitet<br>
      mich seit meiner Kindheit. Mit Fox Moor - Jonas’s<br>
      Guided Stargazing möchte ich dir den<br>
      faszinierenden Sternenhimmel über Lütkau<br>
      (Wendelfurt) näherbringen und dir<br>
      unvergessliche Nächte unter den Sternen<br>
      schenken.
    </p>
    <h2 class="info-heading" style="left:36px; top:329px;">Dein Sternenerlebnis</h2>
    <p class="info-body" style="top:363px;">
      Auf meinen Touren entdeckst du mit mir die<br>
      spannenden Geschichten der griechischen<br>
      Mythologie, die sich hinter unseren<br>
      Sternbildern verbergen. Gemeinsam<br>
      beobachten wir mit leistungsstarkem<br>
      Teleskop und Ferngläsern die Planeten<br>
      unseres Sonnensystems, ferne Galaxien,<br>
      funkelnde Sternhaufen und leuchtende<br>
      Nebel – die Geburtsstätten neuer Sterne.
    </p>
    <p class="info-body info-body-compact" style="top:660px;">
      Außerdem blicke ich mit dir auf<br>
      planetarische Nebel und Supernova-<br>
      Überreste, die vom spektakulären Ende<br>
      eines Sternenlebens erzählen. Touren: 1–2 Std.<br>
      Stühle, Decken, Snacks und Tee<br>
      stelle ich gerne bereit.
    </p>
  </section>

  <svg class="brand-badge" viewBox="0 0 326 326" aria-hidden="true">
    <circle cx="163" cy="163" r="160" fill="#1f5f5c"/>
  </svg>
  <div class="brand-name">Fox Moor</div>

  <div class="portrait" role="img" aria-label="Porträtfoto des Gastgebers neben seinem Teleskop"></div>

  <div class="contact contact-mail">
    <svg class="contact-icon" viewBox="0 0 54 54" aria-hidden="true">
      <circle cx="27" cy="27" r="27" fill="#ffffff"/>
      <rect x="14" y="17" width="26" height="19" rx="2" fill="#5cbcb0"/>
      <polyline points="14,18 27,29 40,18" fill="none" stroke="#ffffff" stroke-width="2.5"/>
    </svg>
    <span>jonas@fox-moor.de</span>
  </div>
  <div class="contact contact-phone">
    <svg class="contact-icon" viewBox="0 0 54 54" aria-hidden="true">
      <circle cx="27" cy="27" r="27" fill="#ffffff"/>
      <path d="M19 15c2-1 3 0 4 2l2 4c1 2 0 3-1 4l-1 1c1 3 3 5 6 6l1-1c1-1 2-2 4-1l4 2c2 1 3 2 2 4l-1 2c-1 2-4 3-7 2-7-2-13-8-15-15-1-3 0-6 2-7z" fill="#1f5f5c"/>
      <path d="M30 16a9 9 0 0 1 8 8M30 21a4 4 0 0 1 3 3" fill="none" stroke="#1f5f5c" stroke-width="2" stroke-linecap="round"/>
    </svg>
    <span>+49 160 5283914</span>
  </div>

  <p class="closing">Ich freue mich darauf, dich bald auf<br>meinen Touren begrüßen zu dürfen.</p>
</main>
</body>
</html>
```